Business Card Design for Small Electrical Contractor

I need to update my business card into something a little more modern. We are a small electrical contracting company. We service domestic and commercial places around Sydney. We have 2 logo designs at the moment. I have uploaded both and 2 different sizes to work with.

Industry/Entity Type

Business

Contact Information for Business Card

Ted Corbin
8/21-23 Holt St, Fernhaven 2087
t - (02) 9471 3820
m - 0427 915 304
E - info@corbinelec.example.au
W - corbinelec.example.au
ABN: 42 907 518 263

Font styles to use
Sans Serif

Requirements
Must have
• I would also like to see the below fit on somewhere aswell
• - Licensed Electrician
• - Level 2 (Cat 1 & 4)
• - Domestic
• - Commercial
• - Repairs and Installations
• - Data
Nice to have
• Try and keep similar colours as logo
Should not have
• No lightning bolts or light globes. Smart and professional please.

```html
<!DOCTYPE html>
<html lang="en">
<head>
<meta charset="utf-8">
<title>Corbin Electrical – Business Card</title>
<link href="https://fonts.googleapis.com/css2?family=Arimo:wght@400;700&display=swap" rel="stylesheet">
<style>
  :root {
    --bg: #d9d9d8;
    --ink: #0b0b0b;
    --paper: #f2f2f0;
    --orange: #f0961c;
    --white: #ffffff;
    --logo-ink: #1d2b25;
  }
  * { box-sizing: border-box; margin: 0; padding: 0; }
  html, body { width: 1200px; height: 960px; overflow: hidden; }
  body {
    background: var(--bg);
    font-family: "Arimo", Arial, sans-serif;
    display: flex;
    flex-direction: column;
    align-items: center;
    justify-content: center;
    gap: 56px;
  }
  .card {
    width: 700px;
    height: 400px;
    position: relative;
    overflow: hidden;
    box-shadow: 0 6px 18px rgba(0,0,0,.18);
  }

  /* Back side */
  .card--back { background: var(--ink); }
  .card--back .brand {
    position: absolute; left: 0; right: 0; top: 110px;
    text-align: center; color: var(--white);
  }
  .brand__name {
    font-weight: 700; font-size: 44px; letter-spacing: 1px;
  }
  .brand__rule {
    width: 300px; height: 3px; background: var(--orange);
    margin: 12px auto 0;
  }
  .services {
    position: absolute; left: 0; right: 0; bottom: 0; height: 112px;
    background: var(--orange);
    display: flex; flex-direction: column; justify-content: center; align-items: center;
    gap: 6px; color: var(--white); font-size: 19px;
  }
  .services__row { display: flex; }
  .services__row span + span { border-left: 2px solid var(--ink); padding-left: 8px; margin-left: 8px; }

  /* Front side */
  .card--front { display: flex; }
  .front__logo {
    width: 50%; background: var(--paper); position: relative;
    display: flex; align-items: center; justify-content: center;
  }
  .front__edge {
    position: absolute; left: 0; top: 28px; bottom: 140px; width: 10px;
    background: var(--orange); border-radius: 0 6px 6px 0;
  }
  .front__logo .brand__name { color: var(--logo-ink); font-size: 34px; text-align: center; }
  .front__logo .brand__rule { width: 230px; }
  .front__contact {
    width: 50%; background: var(--ink); color: var(--white);
    padding: 30px 20px 0 34px;
    display: flex; flex-direction: column; gap: 13px;
  }
  .contact-row { display: flex; align-items: center; gap: 18px; font-size: 16px; line-height: 1.3; }
  .contact-row--name { font-weight: 700; color: var(--orange); font-size: 19px; }
  .icon {
    width: 30px; height: 30px; flex: none; border-radius: 50%;
    background: var(--orange); display: flex; align-items: center; justify-content: center;
  }
  .icon svg { width: 18px; height: 18px; fill: none; stroke: var(--ink); stroke-width: 2; }
  .icon--abn { font-size: 10px; font-weight: 700; color: var(--ink); }
</style>
</head>
<body>

  <section class="card card--back" aria-label="Card back">
    <div class="brand">
      <div class="brand__name">Corbin Electrical</div>
      <div class="brand__rule"></div>
    </div>
    <div class="services">
      <div class="services__row"><span>Licensed Electrician</span><span>Level 2 (Cat 1 &amp; 4)</span><span>Domestic</span></div>
      <div class="services__row"><span>Commercial</span><span>Repairs and Installations</span><span>Data</span></div>
    </div>
  </section>

  <section class="card card--front" aria-label="Card front">
    <div class="front__logo">
      <div class="front__edge"></div>
      <div class="brand">
        <div class="brand__name">Corbin Electrical</div>
        <div class="brand__rule"></div>
      </div>
    </div>
    <div class="front__contact">
      <div class="contact-row contact-row--name">
        <span class="icon"><svg viewBox="0 0 24 24"><circle cx="12" cy="8" r="4"/><path d="M4 21c0-4 4-7 8-7s8 3 8 7"/></svg></span>
        Ted Corbin
      </div>
      <div class="contact-row">
        <span class="icon"><svg viewBox="0 0 24 24"><path d="M12 22s7-7 7-12a7 7 0 0 0-14 0c0 5 7 12 7 12z"/><circle cx="12" cy="10" r="2.5"/></svg></span>
        <span>8/21-23 Holt St,<br>Fernhaven 2087</span>
      </div>
      <div class="contact-row">
        <span class="icon"><svg viewBox="0 0 24 24"><path d="M5 3h4l2 5-3 2a12 12 0 0 0 6 6l2-3 5 2v4a2 2 0 0 1-2 2A18 18 0 0 1 3 5a2 2 0 0 1 2-2z"/></svg></span>
        <span>(02) 9471 3820<br>0427 915 304</span>
      </div>
      <div class="contact-row">
        <span class="icon"><svg viewBox="0 0 24 24"><rect x="3" y="5" width="18" height="14" rx="2"/><path d="M3 7l9 6 9-6"/></svg></span>
        info@corbinelec.example.au
      </div>
      <div class="contact-row">
        <span class="icon"><svg viewBox="0 0 24 24"><circle cx="12" cy="12" r="9"/><path d="M3 12h18M12 3c3 3 3 15 0 18M12 3c-3 3-3 15 0 18"/></svg></span>
        www.corbinelec.example.au
      </div>
      <div class="contact-row">
        <span class="icon icon--abn">abn</span>
        42 907 518 263
      </div>
    </div>
  </section>

</body>
</html>
```